Business Card, A4 Letter Head and DL Envelope for Brandolux

We are looking for a design for our Business Card, A4 Letter Head and DL Envelope.

Brandolux is a distributor of promotional products. We specialize in a range of branded promotional products, these include pens, polo shirts, key rings, drink bottles, uniforms and bags to name a few. We are experts in marketing and assist companies in choosing the right promotional product for their needs. We will predominately be an online business where customers visit our website and browse our range of promotional products and branding options.

Our colours are black, red, white and grey.

Files must be supplied in eps, pdf and ai format.

Please display the following information:
Dorian Pell
Account Manager
Suite xxx, 214 Harwick Lane Melbourne, Victoria 3000
Phone +61 3 5550 1842
Mobile +61 455 501 736
sales@brandolux.example
www.brandolux.example

```html
<!DOCTYPE html>
<html lang="en">
<head>
<meta charset="utf-8">
<title>Brandolux Stationery</title>
<link href="https://fonts.googleapis.com/css2?family=Open+Sans:wght@400;600;700&display=swap" rel="stylesheet">
<style>
  :root {
    --red-dark: #9e1519;
    --red: #c8161d;
    --red-bright: #e3202a;
    --ink: #4a4a4a;
    --grey: #8a8a8a;
    --paper: #ffffff;
    --backdrop: #e4e5e7;
    --font: "Open Sans", Arial, sans-serif;
  }
  * { box-sizing: border-box; margin: 0; padding: 0; }
  html, body { width: 1200px; height: 1000px; overflow: hidden; }
  body { background: var(--backdrop); font-family: var(--font); position: relative; }

  .piece { position: absolute; background: var(--paper); overflow: hidden; }
  .swoosh { position: absolute; inset: 0; width: 100%; height: 100%; }

  .brand { position: absolute; display: flex; align-items: center; gap: 8px; }
  .brand-dot { border-radius: 50%; background: var(--red); flex: none; }
  .brand-name { font-weight: 700; color: var(--ink); letter-spacing: 0.5px; text-transform: uppercase; }
  .brand--light .brand-dot { background: var(--paper); }
  .brand--light .brand-name { color: var(--paper); }

  .contact { position: absolute; color: var(--paper); list-style: none; }
  .contact li { display: flex; align-items: center; gap: 5px; white-space: nowrap; }
  .contact svg { flex: none; fill: var(--paper); }

  /* Letterhead */
  .letterhead { left: 30px; top: 40px; width: 460px; height: 650px; }
  .letterhead .brand { left: 150px; top: 32px; }
  .letterhead .brand-dot { width: 30px; height: 30px; }
  .letterhead .brand-name { font-size: 17px; }
  .letterhead .contact { right: 12px; bottom: 8px; font-size: 6.5px; line-height: 9.5px; }

  /* Envelope back */
  .envelope-back { left: 530px; top: 40px; width: 640px; height: 300px; }
  .envelope-flap {
    position: absolute; left: 0; top: 0; width: 100%; height: 88px;
    background: linear-gradient(90deg, var(--red-dark), var(--red-bright) 50%, var(--red-dark));
    border-radius: 0 0 12px 12px;
  }
  .envelope-back .brand { left: 50%; top: 26px; transform: translateX(-50%); }
  .envelope-back .brand-dot { width: 34px; height: 34px; }
  .envelope-back .brand-name { font-size: 20px; }

  /* Envelope front */
  .envelope-front { left: 530px; top: 370px; width: 640px; height: 300px; }
  .envelope-front .brand { left: 20px; top: 26px; }
  .envelope-front .brand-dot { width: 34px; height: 34px; }
  .envelope-front .brand-name { font-size: 20px; }
  .envelope-front .contact { right: 12px; bottom: 9px; font-size: 7.5px; line-height: 10.5px; }

  /* Business card front */
  .card-front {
    left: 140px; top: 712px; width: 430px; height: 260px;
    background: radial-gradient(ellipse at 50% 45%, var(--red-bright) 0%, var(--red) 40%, var(--red-dark) 100%);
  }
  .card-front .brand { left: 50%; top: 112px; transform: translateX(-50%); }
  .card-front .brand-dot { width: 40px; height: 40px; }
  .card-front .brand-name { font-size: 23px; }
  .card-front .web { position: absolute; right: 110px; bottom: 14px; color: var(--paper); font-size: 12px; }

  /* Business card back */
  .card-back { left: 630px; top: 712px; width: 430px; height: 260px; }
  .card-back .person { position: absolute; right: 30px; top: 20px; text-align: right; }
  .person-name { color: var(--red); font-weight: 700; font-size: 14px; line-height: 18px; }
  .person-role { color: var(--grey); font-size: 12.5px; line-height: 16px; }
  .card-back .brand { left: 24px; top: 96px; }
  .card-back .brand-dot { width: 40px; height: 40px; }
  .card-back .brand-name { font-size: 20px; }
  .card-back .contact { left: 235px; top: 152px; font-size: 12px; line-height: 20px; }
  .card-back .contact .address { display: block; line-height: 17px; margin-bottom: 4px; white-space: normal; }
</style>
</head>
<body>

<!-- A4 letterhead -->
<section class="piece letterhead" aria-label="A4 letterhead">
  <svg class="swoosh" viewBox="0 0 460 650" aria-hidden="true">
    <defs>
      <linearGradient id="lh-red" x1="0" x2="1" y1="0" y2="0">
        <stop offset="0" stop-color="#9e1519"/><stop offset="0.6" stop-color="#e3202a"/><stop offset="1" stop-color="#a3161a"/>
      </linearGradient>
      <linearGradient id="lh-arc" x1="0" x2="1">
        <stop offset="0" stop-color="#2a2a2a"/><stop offset="1" stop-color="#ffffff" stop-opacity="0"/>
      </linearGradient>
    </defs>
    <path d="M0,612 C120,640 300,622 460,552 V650 H0 Z" fill="url(#lh-red)"/>
    <path d="M0,596 C50,622 150,630 240,612 C150,624 60,620 0,604 Z" fill="url(#lh-arc)"/>
  </svg>
  <div class="brand"><span class="brand-dot"></span><span class="brand-name">Brandolux</span></div>
  <ul class="contact">
    <li>Suite xxx, 214 Harwick Lane,</li>
    <li>Melbourne, Victoria 3000</li>
    <li><svg width="6" height="6" viewBox="0 0 10 10"><rect x="1" y="0" width="8" height="10" rx="1"/></svg>+61 3 5550 1842</li>
    <li><svg width="6" height="6" viewBox="0 0 10 10"><rect x="2" y="0" width="6" height="10" rx="1"/></svg>+61 455 501 736</li>
    <li><svg width="6" height="6" viewBox="0 0 10 10"><path d="M0,2 H10 V9 H0 Z"/></svg>sales@brandolux.example</li>
    <li><svg width="6" height="6" viewBox="0 0 10 10"><circle cx="5" cy="5" r="5"/></svg>www.brandolux.example</li>
  </ul>
</section>

<!-- DL envelope, back -->
<section class="piece envelope-back" aria-label="DL envelope back">
  <div class="envelope-flap"></div>
  <div class="brand brand--light"><span class="brand-dot"></span><span class="brand-name">Brandolux</span></div>
</section>

<!-- DL envelope, front -->
<section class="piece envelope-front" aria-label="DL envelope front">
  <svg class="swoosh" viewBox="0 0 640 300" aria-hidden="true">
    <defs>
      <linearGradient id="env-red" x1="0" x2="1">
        <stop offset="0" stop-color="#9e1519"/><stop offset="0.55" stop-color="#e3202a"/><stop offset="1" stop-color="#a3161a"/>
      </linearGradient>
      <linearGradient id="env-arc" x1="0" x2="1">
        <stop offset="0" stop-color="#2a2a2a"/><stop offset="1" stop-color="#ffffff" stop-opacity="0"/>
      </linearGradient>
    </defs>
    <path d="M0,250 C160,300 400,270 640,176 V300 H0 Z" fill="url(#env-red)"/>
    <path d="M0,232 C60,264 180,278 290,262 C180,272 70,258 0,242 Z" fill="url(#env-arc)"/>
  </svg>
  <div class="brand"><span class="brand-dot"></span><span class="brand-name">Brandolux</span></div>
  <ul class="contact">
    <li>Suite xxx, 214 Harwick Lane,</li>
    <li>Melbourne, Victoria 3000</li>
    <li><svg width="7" height="7" viewBox="0 0 10 10"><rect x="1" y="0" width="8" height="10" rx="1"/></svg>+61 3 5550 1842</li>
    <li><svg width="7" height="7" viewBox="0 0 10 10"><rect x="2" y="0" width="6" height="10" rx="1"/></svg>+61 455 501 736</li>
    <li><svg width="7" height="7" viewBox="0 0 10 10"><path d="M0,2 H10 V9 H0 Z"/></svg>sales@brandolux.example</li>
    <li><svg width="7" height="7" viewBox="0 0 10 10"><circle cx="5" cy="5" r="5"/></svg>www.brandolux.example</li>
  </ul>
</section>

<!-- Business card, front -->
<section class="piece card-front" aria-label="Business card front">
  <div class="brand brand--light"><span class="brand-dot"></span><span class="brand-name">Brandolux</span></div>
  <p class="web">www.brandolux.example</p>
</section>

<!-- Business card, back -->
<section class="piece card-back" aria-label="Business card back">
  <svg class="swoosh" viewBox="0 0 430 260" aria-hidden="true">
    <defs>
      <linearGradient id="card-red" x1="0" x2="1">
        <stop offset="0" stop-color="#a3161a"/><stop offset="0.5" stop-color="#c8161d"/><stop offset="1" stop-color="#d81c24"/>
      </linearGradient>
      <linearGradient id="card-arc" x1="0" x2="1">
        <stop offset="0" stop-color="#2a2a2a"/><stop offset="1" stop-color="#ffffff" stop-opacity="0"/>
      </linearGradient>
    </defs>
    <path d="M0,168 C120,215 300,165 430,26 V260 H0 Z" fill="url(#card-red)"/>
    <path d="M0,152 C50,188 150,200 260,176 C150,194 55,178 0,162 Z" fill="url(#card-arc)"/>
  </svg>
  <div class="person">
    <p class="person-name">Dorian Pell</p>
    <p class="person-role">Account Manager</p>
  </div>
  <div class="brand"><span class="brand-dot"></span><span class="brand-name">Brandolux</span></div>
  <ul class="contact">
    <li class="address">Suite xxx, 214 Harwick Lane,<br>Melbourne, Victoria 3000</li>
    <li><svg width="12" height="12" viewBox="0 0 10 10"><path d="M1,1 h3 v3 h-1 v2 h1 v3 h-3 z M5,2 h4 v6 h-4 z"/></svg>+61 3 5550 1842</li>
    <li><svg width="12" height="12" viewBox="0 0 10 10"><path d="M3,0 h4 a1,1 0 0 1 1,1 v8 a1,1 0 0 1 -1,1 h-4 a1,1 0 0 1 -1,-1 v-8 a1,1 0 0 1 1,-1 z M3.5,1.5 v5 h3 v-5 z"/></svg>+61 455 501 736</li>
    <li><svg width="12" height="12" viewBox="0 0 10 10"><path d="M0,4 L5,1 L10,4 V9 H0 Z"/></svg>sales@brandolux.example</li>
  </ul>
</section>

</body>
</html>
```